New Plumbing Company

We are looking for a smart and creative business card design for our new plumbing company. We are looking for creativity and originality in our business cards.

Industry/Entity Type

Plumbing

Contact Information for Business Card

Crestline Plumbing
Peter Halvane
Managing Director
Telephone Number : 0481529604
Email : service@crestlineplumbing.com.au
Website : www.crestlineplumbing.com.au
Lic. 508264K

Colors
0692cd
33a6d7
000000

Requirements
Must have
• I want the business card to be designed on a black background using the blue tones i have selected as seen in the company logo.

```html
<!DOCTYPE html>
<html lang="en">
<head>
<meta charset="utf-8">
<title>Crestline Plumbing – Business Card</title>
<link rel="stylesheet" href="https://fonts.googleapis.com/css2?family=Source+Sans+3:wght@400;600;700&display=swap">
<style>
  :root {
    --blue: #1a7dc2;
    --blue-deep: #0692cd;
    --blue-light: #33a6d7;
    --black: #231f20;
    --white: #ffffff;
    --stage: #eceae6;
    --text-font: "Source Sans 3", "Myriad Pro", sans-serif;
  }
  * { box-sizing: border-box; margin: 0; padding: 0; }
  html, body {
    width: 1200px;
    height: 900px;
    overflow: hidden;
    background: var(--stage);
    font-family: var(--text-font);
  }
  .sheet {
    width: 1200px;
    height: 900px;
    display: flex;
    flex-direction: column;
    align-items: center;
    justify-content: center;
    gap: 40px;
  }
  .card {
    position: relative;
    width: 600px;
    height: 343px;
    overflow: hidden;
    box-shadow: 0 6px 18px rgba(0,0,0,0.18);
  }

  /* Front */
  .card-front { background: var(--blue); }
  .front-ring {
    position: absolute;
    left: 50%;
    top: -30px;
    transform: translateX(-50%);
    width: 200px;
    height: 200px;
    border-radius: 50%;
    border: 3px solid rgba(0,0,0,0.10);
    box-shadow: 0 1px 0 rgba(255,255,255,0.15);
  }
  .front-name {
    position: absolute;
    left: 0;
    right: 0;
    top: 190px;
    text-align: center;
    color: var(--white);
    font-weight: 400;
    font-size: 50px;
    letter-spacing: 0.5px;
  }

  /* Back */
  .card-back { background: var(--black); color: var(--white); }
  .contact {
    position: absolute;
    left: 330px;
    top: 48px;
  }
  .person-name {
    color: var(--blue);
    font-weight: 700;
    font-size: 17px;
    line-height: 1.1;
  }
  .person-role {
    font-size: 13px;
    line-height: 1.3;
  }
  .licence {
    margin-top: 22px;
    font-weight: 700;
    font-size: 15px;
  }
  .contact-list {
    list-style: none;
    margin-top: 16px;
  }
  .contact-list li {
    display: flex;
    align-items: center;
    gap: 10px;
    font-size: 13px;
    line-height: 22px;
  }
  .contact-list svg { width: 11px; height: 11px; fill: var(--blue); flex: none; }
  .brand {
    position: absolute;
    left: 40px;
    bottom: 48px;
    display: flex;
    align-items: center;
    gap: 12px;
  }
  .brand-dot {
    width: 44px;
    height: 44px;
    border-radius: 50%;
    border: 3px solid var(--blue);
  }
  .brand-name {
    color: var(--white);
    font-weight: 400;
    font-size: 30px;
  }
</style>
</head>
<body>
<main class="sheet">
  <section class="card card-front" aria-label="Card front">
    <div class="front-ring" aria-hidden="true"></div>
    <h1 class="front-name">Crestline Plumbing</h1>
  </section>

  <section class="card card-back" aria-label="Card back">
    <div class="contact">
      <p class="person-name">Peter Halvane</p>
      <p class="person-role">Managing Director</p>
      <p class="licence">Lic. 508264K</p>
      <ul class="contact-list">
        <li>
          <svg viewBox="0 0 24 24" aria-hidden="true"><path d="M6.6 10.8a15.1 15.1 0 0 0 6.6 6.6l2.2-2.2a1 1 0 0 1 1-.25 11.4 11.4 0 0 0 3.6.57 1 1 0 0 1 1 1V20a1 1 0 0 1-1 1A17 17 0 0 1 3 4a1 1 0 0 1 1-1h3.5a1 1 0 0 1 1 1c0 1.25.2 2.45.57 3.57a1 1 0 0 1-.25 1z"/></svg>
          0481529604
        </li>
        <li>
          <svg viewBox="0 0 24 24" aria-hidden="true"><path d="M2 5h20v14H2z M2 5l10 8 10-8" /></svg>
          service@crestlineplumbing.com.au
        </li>
        <li>
          <svg viewBox="0 0 24 24" aria-hidden="true"><path d="M10.6 13.4a1 1 0 0 1 0-1.4l3-3a1 1 0 1 1 1.4 1.4l-3 3a1 1 0 0 1-1.4 0zM8 20a4 4 0 0 1-2.8-6.8l2.5-2.5 1.4 1.4-2.5 2.5a2 2 0 1 0 2.8 2.8l2.5-2.5 1.4 1.4-2.5 2.5A4 4 0 0 1 8 20zm8.3-6.7-1.4-1.4 2.5-2.5a2 2 0 1 0-2.8-2.8l-2.5 2.5-1.4-1.4 2.5-2.5a4 4 0 0 1 5.6 5.6z"/></svg>
          www.crestlineplumbing.com.au
        </li>
      </ul>
    </div>
    <div class="brand">
      <span class="brand-dot" aria-hidden="true"></span>
      <span class="brand-name">Crestline Plumbing</span>
    </div>
  </section>
</main>
</body>
</html>
```